Building certification business in Sydney Australia

Brookvale Assessors is a small business that is currently growing and needs a profession looking website to attract customers and give them all the information they need. The main services we offer currently are pre-purchase building inspections for purchasers and other areas of construction consultancy including pool fencing certificates. Please see attached logos to incorporate to also match colour schemes with. Thanks!

Target Market(s)

Prospective buyers and home owners

Industry/Entity Type

Small Business

Requirements
Must have
• Promote the main services from the home page. Being able to select the type of service/certificate required from the main page and be directed to a specific page that deals with only that service containing the relevant information for that item.
Nice to have
• Small emphasis on the location of our office and areas we service etc.

```html
<!DOCTYPE html>
<html lang="en">
<head>
<meta charset="utf-8">
<title>Brookvale Assessors</title>
<link href="https://fonts.googleapis.com/css2?family=Arimo:wght@400;700&family=Roboto:wght@300;400&display=swap" rel="stylesheet">
<style>
:root{
  --blue:#3d8ec9;
  --navy:#223a52;
  --text:#666;
  --text-dark:#555;
  --muted:#888;
  --band:#efefef;
  --bar:#f2f2f2;
  --line:#dcdcdc;
  --white:#fff;
  --dark-btn:#3c3c3c;
}
*{margin:0;padding:0;box-sizing:border-box}
html,body{width:1200px;height:1000px;overflow:hidden;background:var(--white);font-family:"Arimo",Arial,sans-serif;color:var(--text)}
.page{position:relative;width:1200px;height:1000px}
.abs{position:absolute}

/* header */
.brand{left:194px;top:22px;display:flex;align-items:center;gap:10px}
.brand-mark{width:50px;height:50px;background:var(--navy);border-radius:6px}
.brand-name{font-size:24px;font-weight:700;color:var(--navy);line-height:1.05;width:140px}
.social{left:840px;top:47px;display:flex;gap:3px}
.social-btn{height:16px;padding:0 5px;border:1px solid #cfcfcf;border-radius:2px;background:linear-gradient(#fff,#eee);font-size:8.5px;line-height:14px;color:#555}

/* nav */
.navbar{left:0;top:97px;width:1200px;height:44px;background:var(--bar);border-top:1px solid #e4e4e4}
.nav-accent{left:0;top:141px;width:1200px;height:4px;background:var(--blue)}
.nav-item{top:115px;font-size:11.5px;color:var(--text-dark);list-style:none}
.nav-item.active{color:var(--blue)}
.search{left:840px;top:103px;width:155px;height:31px;background:var(--white);border-radius:2px;display:flex;align-items:center;padding-left:10px;gap:9px;font-size:10px;font-style:italic;color:#999}

/* hero */
.hero{left:0;top:145px;width:1200px;height:396px;background:var(--band);border-bottom:1px solid #e2e2e2}
.hero-title{left:194px;top:260px;font-size:30px;font-weight:400;color:var(--text);letter-spacing:.3px;line-height:36px}
.hero-title strong{display:block;color:var(--blue);font-weight:700;font-size:29px}
.hero-copy{left:194px;top:340px;width:385px;font-size:11.3px;line-height:15px;color:var(--text)}
.hero-nav{left:195px;top:387px;display:flex;gap:6px}
.hero-arrow{width:27px;height:27px;border-radius:50%;border:2px solid #ddd;color:#fff;font-size:11px;line-height:23px;text-align:center}
.hero-arrow.prev{background:var(--blue)}
.hero-arrow.next{background:var(--dark-btn)}
.hero-visual{left:700px;top:200px;width:230px;height:285px;background:linear-gradient(160deg,#e9e9e9,#e4dcc4 55%,#dedede)}
.cert-badge{left:644px;top:410px;width:98px;height:98px;border-radius:50%;background:var(--blue);color:#fff;font-size:11px;font-weight:700;display:flex;align-items:center;justify-content:center}

/* welcome */
.welcome{left:0;top:590px;width:1200px;text-align:center;font-family:"Roboto",Arial,sans-serif;font-weight:300;font-size:24px;color:var(--text)}
.welcome span{color:var(--blue)}
.welcome-copy{left:270px;top:632px;width:660px;text-align:center;font-size:10.8px;line-height:15px;color:var(--text)}
.divider{left:194px;top:701px;width:800px;height:4px;background:var(--blue)}

/* services */
.service{top:735px;width:174px}
.service-photo{height:110px}
.service h3{margin-top:11px;font-size:12px;font-weight:700;color:var(--text)}
.service a{display:block;margin-top:3px;font-size:10px;color:var(--blue);text-decoration:none}
.links{left:777px;top:731px;width:217px}
.links h2{font-size:15px;font-weight:400;color:var(--text);padding-bottom:7px;border-bottom:2px solid var(--line)}
.links h2 strong{color:var(--blue)}
.links ul{list-style:none;margin-top:9px}
.links li{display:flex;align-items:center;gap:8px;font-size:11.5px;color:var(--text-dark);height:21px}
.links li.current span{color:var(--blue);text-decoration:underline}
.links li:nth-child(4){margin-top:2px}

/* footer */
.footer-line{left:0;top:945px;width:1200px;height:1px;background:var(--line)}
.copyright{left:195px;top:959px;font-size:10px;color:var(--muted)}
.footer-nav{right:206px;top:959px;font-size:10px;color:var(--muted)}
.footer-nav .active{color:var(--blue);text-decoration:underline}
</style>
</head>
<body>
<div class="page">

  <header>
    <div class="abs brand"><div class="brand-mark"></div><div class="brand-name">Brookvale Assessors</div></div>
    <div class="abs social">
      <span class="social-btn">Chirper</span>
      <span class="social-btn">Facepage</span>
      <span class="social-btn">Searchly</span>
    </div>
  </header>

  <div class="abs navbar"></div>
  <ul>
    <li class="abs nav-item active" style="left:194px">HOME</li>
    <li class="abs nav-item" style="left:261px">ABOUT US</li>
    <li class="abs nav-item" style="left:348px">SERVICES</li>
    <li class="abs nav-item" style="left:435px">CONSULTING</li>
    <li class="abs nav-item" style="left:530px">CONTACT US</li>
  </ul>
  <div class="abs search">
    <svg width="11" height="11" viewBox="0 0 11 11"><circle cx="4.5" cy="4.5" r="3.3" fill="none" stroke="#999" stroke-width="1.4"/><line x1="7" y1="7" x2="10" y2="10" stroke="#999" stroke-width="1.6"/></svg>
    Search Keywords
  </div>
  <div class="abs nav-accent"></div>

  <section class="abs hero"></section>
  <h1 class="abs hero-title">YOUR SUCCESS IS OUR<strong>BUSINESS</strong></h1>
  <p class="abs hero-copy">Lorem Ipsum is simply dummy text of the printing and typesetting industry. Lorem Ipsum has been the industry's standard dummy text ever since</p>
  <div class="abs hero-nav"><span class="hero-arrow prev">&laquo;</span><span class="hero-arrow next">&raquo;</span></div>
  <div class="abs hero-visual" role="img" aria-label="Illustration of a glowing light bulb with a pencil and service icons"></div>
  <div class="abs cert-badge">CERTIFICATES</div>

  <h2 class="abs welcome">Welcome to Brookvale <span>ASSESSORS!</span></h2>
  <p class="abs welcome-copy">Lorem Ipsum is simply dummy text of the printing and typesetting industry. Lorem Ipsum has been the industry's standard dummy text ever since the 1500s, when an unknown printer took a galley of type and scrambled it to make a type specimen book.</p>
  <div class="abs divider"></div>

  <article class="abs service" style="left:194px">
    <div class="service-photo" role="img" aria-label="Photo of hands at a laptop reviewing charts" style="background:linear-gradient(135deg,#e9edf2,#b9c2cc)"></div>
    <h3>Pre-purchase Building</h3><a href="#">Lorem Ipsum is simply dummy text</a>
  </article>
  <article class="abs service" style="left:378px">
    <div class="service-photo" role="img" aria-label="Photo of a consultant with a team in an office" style="background:linear-gradient(135deg,#e7d9c6,#8a6a4e)"></div>
    <h3>Pool Fencing</h3><a href="#">Lorem Ipsum is simply dummy text</a>
  </article>
  <article class="abs service" style="left:561px">
    <div class="service-photo" role="img" aria-label="Photo of a businessman on the phone with an engineer on site" style="background:linear-gradient(135deg,#dfe3e8,#8d9aa8)"></div>
    <h3>Construction Consultancy</h3><a href="#">&nbsp;Lorem Ipsum is simply dummy text</a>
  </article>

  <aside class="abs links">
    <h2>SERVICES <strong>LINKS</strong></h2>
    <ul>
      <li><svg width="13" height="13" viewBox="0 0 13 13"><circle cx="6.5" cy="6.5" r="6" fill="#3a3a3a" stroke="#ccc"/><path d="M4 6.7l1.7 1.6L9 5" fill="none" stroke="#fff" stroke-width="1.3"/></svg><span>Pool Fencing Certificates</span></li>
      <li class="current"><svg width="13" height="13" viewBox="0 0 13 13"><circle cx="6.5" cy="6.5" r="6" fill="#3a3a3a" stroke="#ccc"/><path d="M4 6.7l1.7 1.6L9 5" fill="none" stroke="#fff" stroke-width="1.3"/></svg><span>Construction Consultancy</span></li>
      <li><svg width="13" height="13" viewBox="0 0 13 13"><circle cx="6.5" cy="6.5" r="6" fill="#3a3a3a" stroke="#ccc"/><path d="M4 6.7l1.7 1.6L9 5" fill="none" stroke="#fff" stroke-width="1.3"/></svg><span>Pre-purchase Building Inspections</span></li>
      <li><svg width="13" height="13" viewBox="0 0 13 13"><circle cx="6.5" cy="6.5" r="6" fill="#3a3a3a" stroke="#ccc"/><path d="M4 6.7l1.7 1.6L9 5" fill="none" stroke="#fff" stroke-width="1.3"/></svg><span>Pool Fencing Certificates</span></li>
      <li><svg width="13" height="13" viewBox="0 0 13 13"><circle cx="6.5" cy="6.5" r="6" fill="#3a3a3a" stroke="#ccc"/><path d="M4 6.7l1.7 1.6L9 5" fill="none" stroke="#fff" stroke-width="1.3"/></svg><span>Construction Consultancy</span></li>
    </ul>
  </aside>

  <footer>
    <div class="abs footer-line"></div>
    <p class="abs copyright">Copyright &copy; 2014 Company Name.</p>
    <p class="abs footer-nav"><span class="active">Home</span> &nbsp;|&nbsp; About Us &nbsp;|&nbsp; Services &nbsp;|&nbsp; Consultancy &nbsp;|&nbsp; Contact Us</p>
  </footer>
</div>
</body>
</html>
```